Bay & Meadow Property Services Tri-fold sales & marketing brochure

We need a tri-fold brochure that describes our three lines of business and the various services within each line to use in sales and marketing efforts.
See website for additional background info:
https://halvernq7.example-host.com/

Target Market(s)

Real Estate Investors & owners in Residential Rental, Short-term Rentals, and Mini/Maxi Storage Rental markets

Requirements
Must have
• See attached logo, use color scheme & font styles to match. Make sure to utilize photos to enhance look/feel.

```html
<!DOCTYPE html>
<html lang="en">
<head>
<meta charset="utf-8">
<title>Bay &amp; Meadow Property Services – Tri-fold Brochure</title>
<link rel="stylesheet" href="https://fonts.googleapis.com/css2?family=Cinzel:wght@500;600;700&family=Montserrat:ital,wght@0,400;0,500;0,600;0,700;1,400;1,500&display=swap">
<style>
:root{
  --navy:#0c4a5c;
  --navy-deep:#083c4c;
  --teal:#1b9fc5;
  --teal-bright:#22b0d6;
  --sky:#2a9fd3;
  --pale:#e3e6c5;
  --paper:#ffffff;
  --ink:#2d3a40;
  --muted:#55646a;
  --stage:#d6d8da;
}
*{box-sizing:border-box;margin:0;padding:0}
html,body{width:803px;height:1200px;overflow:hidden}
body{background:var(--stage);font-family:"Montserrat",Arial,sans-serif;color:var(--ink);position:relative}
.spread{position:absolute;left:20px;width:763px;height:537px;background:var(--paper);overflow:hidden;box-shadow:0 4px 14px rgba(0,0,0,.22)}
.spread--outside{top:45px}
.spread--inside{top:620px}
.spread-art{position:absolute;inset:0;width:763px;height:537px}
.abs{position:absolute}
.heading{font-family:"Cinzel",Georgia,serif;font-weight:600;line-height:1.05;letter-spacing:.2px}
.body-text{font-size:6.1px;line-height:1.42;color:var(--muted)}
.photo{position:absolute}
/* lists */
.service-list{list-style:none}
.service-list li{position:relative;padding-left:11px;margin-bottom:7px;font-size:5.6px;line-height:1.4;color:var(--muted)}
.service-list li strong{display:block;font-weight:700;color:var(--ink);font-size:6px}
.service-list li::before{content:"";position:absolute;left:0;top:1px;width:6px;height:6px;border-radius:50%;background:var(--teal)}
.service-list li::after{content:"";position:absolute;left:1.8px;top:2.4px;width:1.6px;height:2.6px;border:solid #fff;border-width:0 1px 1px 0;transform:rotate(45deg)}
.service-list--light li{color:#d4e6ec}
.service-list--light li strong{color:#fff}
.service-list--light li::before{background:#fff}
.service-list--light li::after{border-color:var(--navy)}
.box-title{font-family:"Cinzel",Georgia,serif;font-weight:600;font-size:9.5px;color:var(--teal);margin-bottom:9px}
/* outside */
.intro{left:28px;top:22px;width:200px;font-size:7px;font-style:italic;line-height:1.4;color:var(--ink)}
.expertise-box{left:22px;top:108px;width:212px;height:218px;border-radius:14px;padding:14px 14px;background:linear-gradient(100deg,#eef1d9 0%,#cfe3da 55%,#8ec9d5 100%)}
.expertise-box .box-title{color:var(--navy);font-size:10px}
.expertise-box .service-list li{font-style:italic;margin-bottom:6px}
.expertise-box .service-list li strong{font-style:normal}
.tagline{left:268px;top:16px;width:230px}
.tagline .t1{font-size:14px;color:var(--navy)}
.tagline .t2{font-size:16px;color:var(--teal);margin-top:1px}
.tagline .t3{font-family:"Cinzel",Georgia,serif;font-size:6px;font-weight:700;color:var(--navy);margin-top:3px}
.brand{display:flex;align-items:center;gap:7px;font-family:"Cinzel",Georgia,serif;font-weight:600;color:var(--navy)}
.brand-dot{width:12px;height:12px;border-radius:50%;background:var(--teal);flex:none}
.brand--top{left:548px;top:20px;width:200px;font-size:11px;line-height:1.15}
.contact-block{left:284px;top:282px;width:202px;color:#fff;text-align:left}
.contact-pill{border:1.5px solid var(--teal-bright);border-radius:12px;text-align:center;font-family:"Cinzel",Georgia,serif;font-weight:600;font-size:13px;padding:3px 0 2px;color:#fff}
.phone{display:flex;align-items:center;gap:4px;font-size:21px;font-weight:500;margin-top:9px;letter-spacing:.2px}
.contact-line{display:flex;align-items:center;gap:4px;font-size:6.2px;margin-top:4px}
.contact-line span.dot{width:5px;height:5px;border-radius:50%;background:#fff;flex:none}
.brand--back{left:296px;top:420px;width:180px;flex-direction:column;gap:9px;color:#fff;font-size:11px;text-align:center;line-height:1.2}
.brand--back .brand-dot{width:34px;height:34px;background:var(--teal-bright)}
.headline{left:528px;top:272px;width:222px;text-align:center}
.headline .h1{font-size:14.5px;color:var(--navy)}
.headline .h2{font-size:14.5px;color:var(--teal)}
.headline p{font-size:6.3px;line-height:1.45;color:var(--ink);margin-top:9px}
.headline p b{font-weight:700}
.footer-url{left:560px;top:512px;color:#fff;font-size:10.5px;font-weight:600;display:flex;align-items:center;gap:4px}
.footer-url .dot{width:7px;height:7px;border-radius:50%;border:1.5px solid #fff}
/* inside */
.sector-title{font-size:11px;color:var(--teal)}
.panel-copy{width:205px}
.services-box{border:1.5px solid var(--teal);border-radius:12px;padding:12px 12px 4px;background:#fff}
.services-box--dark{border-color:var(--teal-bright);background:transparent}
.services-box--dark .box-title{color:#fff}
.mid-copy .body-text{color:#d6e7ec}
</style>
</head>
<body>

<!-- OUTSIDE SPREAD -->
<section class="spread spread--outside" aria-label="Brochure outside: flap, back and cover">
  <svg class="spread-art" viewBox="0 0 763 537" aria-hidden="true">
    <defs>
      <linearGradient id="aerial" x1="0" y1="0" x2="0" y2="1">
        <stop offset="0" stop-color="#bcdcf0"/>
        <stop offset=".35" stop-color="#7fae63"/>
        <stop offset=".7" stop-color="#8b7a62"/>
        <stop offset="1" stop-color="#5f8a45"/>
      </linearGradient>
      <linearGradient id="hand" x1="0" y1="0" x2="1" y2="1">
        <stop offset="0" stop-color="#d9e3ea"/>
        <stop offset=".6" stop-color="#d9b59b"/>
        <stop offset="1" stop-color="#b7794e"/>
      </linearGradient>
    </defs>
    <!-- navy back panel -->
    <rect x="262" y="235" width="248" height="302" fill="var(--navy)"/>
    <!-- aerial photo over middle and cover -->
    <path d="M234 70 H763 V230 C680 205 600 215 520 255 C470 230 380 222 262 240 Q240 150 234 70Z" fill="url(#aerial)" role="img" aria-label="Aerial photo of a suburban housing estate among green fields"/>
    <path d="M262 240 C380 222 470 230 520 255 C600 215 680 205 763 230 V240 C680 218 600 226 520 264 C470 240 380 232 262 250Z" fill="var(--teal)"/>
    <!-- bottom bands -->
    <path d="M0 470 C180 440 420 455 763 480 V537 H0Z" fill="var(--pale)"/>
    <path d="M0 482 C200 458 430 470 763 493 V537 H0Z" fill="var(--teal)"/>
    <path d="M0 500 C220 478 460 490 763 505 V537 H0Z" fill="var(--sky)"/>
    <rect x="262" y="235" width="248" height="302" fill="var(--navy)" opacity="0"/>
    <path d="M262 250 V537 H510 V262 C470 242 380 235 262 250Z" fill="var(--navy)"/>
    <!-- circular flap photo -->
    <circle cx="96" cy="425" r="74" fill="var(--teal)"/>
    <circle cx="96" cy="425" r="70" fill="#fff"/>
    <circle cx="96" cy="425" r="67" fill="url(#hand)" role="img" aria-label="Photo of hands holding a small model house over paperwork"/>
  </svg>

  <p class="abs intro">Whether you're a seasoned investor or a first-time property owner, Bay &amp; Meadow Property Services offers the insight, care, and results-driven strategies you need. Experience the difference of personalized, white-glove service and see your property reach its full potential.</p>

  <div class="abs expertise-box">
    <h3 class="box-title">Our Expertise Includes:</h3>
    <ul class="service-list">
      <li><strong>Investment &amp; Opportunity Evaluation:</strong>Finding and analyzing lucrative real estate projects tailored to your goals.</li>
      <li><strong>Design &amp; Project Management</strong>Overseeing new construction or refurbishment projects to enhance property value.</li>
      <li><strong>Compliance &amp; Operationalization:</strong>Navigating local regulations and preparing properties for occupancy with minimal vacancies.</li>
      <li><strong>Tenant &amp; Property Management:</strong>Providing seamless day-to-day management for tenants and properties to ensure optimal satisfaction and financial performance.</li>
      <li><strong>Strategic Exits:</strong>Guiding you through the sale process to secure top dollar for your investments.</li>
    </ul>
  </div>

  <div class="abs tagline">
    <div class="heading t1">Maximize Value.</div>
    <div class="heading t2">Maximize Returns.</div>
    <div class="t3">Welcome to the Bay &amp; Meadow Difference.</div>
  </div>

  <div class="abs brand brand--top"><span class="brand-dot"></span><span>Bay &amp; Meadow<br>Property Services</span></div>

  <div class="abs contact-block">
    <div class="contact-pill">Contact Us</div>
    <div class="phone">
      <svg width="14" height="16" viewBox="0 0 24 24" aria-hidden="true"><path fill="#fff" d="M6.6 10.8a15 15 0 0 0 6.6 6.6l2.2-2.2c.3-.3.7-.4 1-.2 1.1.4 2.3.6 3.6.6.6 0 1 .4 1 1V20c0 .6-.4 1-1 1A17 17 0 0 1 3 4c0-.6.4-1 1-1h3.5c.6 0 1 .4 1 1 0 1.3.2 2.5.6 3.6.1.3 0 .7-.2 1z"/></svg>
      (555) 014-2290
    </div>
    <div class="contact-line"><span class="dot"></span>info@bayandmeadowproperty.example</div>
    <div class="contact-line"><span class="dot"></span>www.halvernq7.example-host.com</div>
  </div>

  <div class="abs brand brand--back"><span class="brand-dot"></span><span>Bay &amp; Meadow<br>Property Services</span></div>

  <div class="abs headline">
    <div class="heading h1">Where Expertise</div>
    <div class="heading h2">Meets Exceptional</div>
    <div class="heading h1">Returns</div>
    <p>At Bay &amp; Meadow Property Services, we are your trusted partner in unlocking the full potential of your real estate investments. With unparalleled expertise across three key sectors—<b>long-term residential rentals, short-term vacation rentals</b> (like VacaLoft and StayNest), and <b>mini-maxi storage</b></p>
  </div>

  <div class="abs footer-url"><span class="dot"></span>halvernq7.example-host.com</div>
</section>

<!-- INSIDE SPREAD -->
<section class="spread spread--inside" aria-label="Brochure inside: three business sectors">
  <svg class="spread-art" viewBox="0 0 763 537" aria-hidden="true">
    <defs>
      <linearGradient id="homes" x1="0" y1="0" x2="0" y2="1">
        <stop offset="0" stop-color="#a9cfee"/><stop offset=".55" stop-color="#d8d4cc"/><stop offset="1" stop-color="#6f8f52"/>
      </linearGradient>
      <linearGradient id="storage" x1="0" y1="0" x2="0" y2="1">
        <stop offset="0" stop-color="#8fc0ec"/><stop offset=".45" stop-color="#3f66a8"/><stop offset="1" stop-color="#9a9ea2"/>
      </linearGradient>
      <linearGradient id="desk" x1="0" y1="0" x2="1" y2="1">
        <stop offset="0" stop-color="#dfe6ec"/><stop offset=".6" stop-color="#e7d0bd"/><stop offset="1" stop-color="#b9bfc4"/>
      </linearGradient>
    </defs>
    <rect x="254" y="0" width="254" height="537" fill="var(--navy)"/>
    <path d="M0 0 H234 V112 C150 130 70 128 0 118Z" fill="url(#homes)" role="img" aria-label="Photo of modern terraced townhouses on a sunny street"/>
    <path d="M0 118 C70 128 150 130 234 112 V118 C150 136 70 134 0 124Z" fill="var(--teal)"/>
    <path d="M508 0 H763 V170 C680 165 590 160 508 150Z" fill="url(#storage)" role="img" aria-label="Photo of a self-storage building with blue roller doors"/>
    <path d="M508 150 C590 160 680 165 763 170 V176 C680 171 590 166 508 156Z" fill="var(--teal)"/>
    <rect x="272" y="420" width="218" height="88" rx="10" fill="url(#desk)" role="img" aria-label="Photo of hands using a calculator beside a small model house"/>
    <path d="M0 490 C200 470 470 476 763 488 V537 H0Z" fill="var(--pale)"/>
    <path d="M0 500 C220 482 480 488 763 498 V537 H0Z" fill="var(--teal)"/>
    <path d="M0 515 C240 500 500 506 763 512 V537 H0Z" fill="var(--sky)"/>
  </svg>

  <div class="abs panel-copy" style="left:24px;top:138px">
    <h2 class="heading sector-title">Residential Rental<br>Real Estate Sector</h2>
    <p class="body-text" style="margin-top:6px">Residential rentals offer tenants a wide array of living options that cater to diverse lifestyles and budgetary needs. With trends increasingly favoring properties that support remote work, tenants now seek rentals with dedicated workspaces and robust internet connectivity. Urban apartments remain popular for their proximity to amenities and employment centers, while suburban rentals attract those desiring more space and a quieter environment. This sector's evolution continues to be shaped by changing demographics, economic factors, and a shift towards more flexible living arrangements.</p>
  </div>
  <div class="abs services-box" style="left:20px;top:296px;width:212px;height:196px">
    <h3 class="box-title">Our Services Include:</h3>
    <ul class="service-list">
      <li><strong>Market Research &amp; Feasibility Analysis</strong>In-depth analysis of neighborhood trends, rental demand, and projected ROI to identify prime investment zones.</li>
      <li><strong>Off-Market Property Sourcing</strong>Access to exclusive, off-market listings and distressed assets with potential for high-value returns.</li>
      <li><strong>Investment Matching</strong>Tailored property/project recommendations based on your financial goals, risk profile, and portfolio strategy.</li>
      <li><strong>Due Diligence Support</strong>Evaluation of zoning, title, environmental, and neighborhood metrics to vet and validate opportunities.</li>
      <li><strong>Redevelopment Potential Identification</strong>Pinpointing properties suited for repositioning or conversion (e.g., single to multi-unit, tear-down &amp; rebuild, etc.)</li>
    </ul>
  </div>

  <div class="abs panel-copy mid-copy" style="left:276px;top:18px;width:212px">
    <h2 class="heading sector-title" style="color:#fff">Short-Term Rental<br>Real Estate Sector</h2>
    <p class="body-text" style="margin-top:6px">The short-term rental sector is a dynamic and rapidly expanding segment of the greater real estate market, offering unique opportunities for property owners and investors. Driven by platforms like StayNest and VacaLoft, this market caters to travelers seeking homely accommodations for brief periods, providing a lucrative alternative to traditional hotel stays. Short-term rentals appeal to a broad demographic, from tourists and business travelers to families and remote workers looking for a change of scenery.</p>
    <p class="body-text" style="margin-top:6px">This sector is particularly attractive due to its flexibility in pricing and the ability to generate higher per-night revenues compared to long-term rentals.</p>
  </div>
  <div class="abs services-box services-box--dark" style="left:272px;top:192px;width:218px;height:212px">
    <h3 class="box-title">Our Services Include:</h3>
    <ul class="service-list service-list--light">
      <li><strong>Locating STR Project / Investment Opportunities</strong>Gain access to exclusive listings and data-informed insights on high-performing STR zones and undervalued properties ready for conversion.</li>
      <li><strong>ROI &amp; Occupancy Forecasting</strong>Analyze nightly rates, local demand cycles, and booking performance to determine realistic yield expectations.</li>
      <li><strong>Off-Market Sourcing</strong>We find STR-suitable homes and properties before they hit the open market, with a focus on zoning compatibility and traveler appeal.</li>
      <li><strong>Market Positioning &amp; Audience Targeting</strong>Evaluate your location's appeal to travelers and curate listings to outperform in competitive markets.</li>
    </ul>
  </div>

  <div class="abs panel-copy" style="left:530px;top:178px;width:210px">
    <h2 class="heading sector-title">Mini &amp; Maxi Storage<br>Real Estate Sector</h2>
    <p class="body-text" style="margin-top:6px">Mini storage facilities, offering compact, secure units, cater to individuals and small businesses seeking space-efficient solutions for personal belongings, documents, or inventory. Maxi storage, on the other hand, provides expansive areas designed for large-scale storage needs, accommodating everything from substantial business merchandise to recreational vehicles. Most facilities are incorporating both styles of storage to increase demand and attract a diverse customer base.</p>
  </div>
  <div class="abs services-box" style="left:526px;top:322px;width:214px;height:166px">
    <h3 class="box-title">Our Services Include:</h3>
    <ul class="service-list">
      <li><strong>Locating Project / Investment Opportunities</strong>We uncover high-potential land and conversion assets ideal for self-storage development—before they become publicly available.</li>
      <li><strong>Feasibility Studies &amp; Market Analysis</strong>Analyze demand drivers, competitive landscape, and zoning constraints to validate project viability.</li>
      <li><strong>Off-Market Site Sourcing</strong>Access a pipeline of unlisted properties with optimal location metrics for mini and maxi storage facilities.</li>
      <li><strong>Investment Planning &amp; Portfolio Strategy</strong>Tailored recommendations that align with your capital goals, market risk, and desired scale.</li>
    </ul>
  </div>
</section>

</body>
</html>
```